Custom Home Page for our new Website

We need a custom home page designed for our new website. We are a successful local copier dealer who is rebuilding our website from scratch. We have decided on Wordpress as our CMS platform and have purchased the professional Corvan theme.

The custom homepage we want will be an imitation of the screen on latest model of copiers we carry. (A picture of this is attached.) the goal is to imitate this style while creating a unique, user-friendly, helpful portal to our website.

The winning entry will make the best transition between the menu structure of our current website (www.plomra.net) and the new layout.

Target Market(s)

Our target market is small to medium sized businesses in the Southeast US. The users of our site are generally IT professionals looking for drivers/support, gatekeepers or other support staff placing service calls and supply orders or prospects looking for information about our company and products.

Requirements
Must have
• Clean design, no distracting elements
• Modern aesthetic
• A color palette that can be used as a basis for the Skin for the rest of the site (The site's look will be based on the winning homepage design.)
• Simple navigation
• Easy to read
• Easily viewed on both desktop and tablet sized screens
• Our logo
• Easily update-able
• Maximum of 4 of the large squares

```html
<!DOCTYPE html>
<html lang="en">
<head>
<meta charset="utf-8">
<title>V7 – Home</title>
<link href="https://fonts.googleapis.com/css2?family=Roboto+Condensed:wght@400;700&family=Open+Sans:wght@400;600&display=swap" rel="stylesheet">
<style>
:root{
  --red:#c8102e;
  --red-dark:#7e0818;
  --red-text:#b0141f;
  --ink:#111;
  --body:#666;
  --light:#f7f7f2;
  --grey-band:#f1f1f1;
  --footer:#0f0f0f;
  --footer-bar:#1b1b1b;
  --footer-link:#aaa;
  --yellow:#f6b400;
  --green:#5c9a1c;
}
*{margin:0;padding:0;box-sizing:border-box}
html,body{width:897px;height:1200px;overflow:hidden}
body{position:relative;font-family:"Open Sans",Arial,sans-serif;background:#fff;color:var(--body)}

/* header */
.site-header{position:absolute;left:0;top:0;width:897px;height:88px;
  background:linear-gradient(#e3112f 0%,#c30d27 55%,#6e0614 100%)}
.brand{position:absolute;left:108px;top:20px;display:flex;align-items:center;gap:8px;
  font-family:"Roboto Condensed",sans-serif;font-weight:700;font-size:38px;color:#fff;line-height:1}
.brand-dot{width:14px;height:14px;background:#fff;border-radius:50%}
.call{position:absolute;right:107px;top:22px;font-family:"Roboto Condensed",sans-serif;font-size:15px;color:#fff}
.main-nav{position:absolute;left:366px;top:64px;height:24px;display:flex}
.main-nav a{display:block;flex:0 0 auto;height:24px;line-height:24px;text-align:center;color:#fff;text-decoration:none;
  white-space:nowrap;font-family:"Roboto Condensed",sans-serif;font-weight:700;font-size:14px;
  background:linear-gradient(#2a2a2a,#0d0d0d);transform:skewX(-20deg);margin-right:2px}
.main-nav a span{display:inline-block;transform:skewX(20deg)}
.main-nav a.active{background:var(--red)}
.nav-home{width:64px}.nav-who{width:86px}.nav-offer{width:102px}.nav-support{width:72px}.nav-contact{width:86px}

/* hero */
.hero{position:absolute;left:0;top:88px;width:897px;height:350px;
  background:radial-gradient(ellipse at 60% 40%,#4a4d52 0%,#2a2c30 45%,#15161a 100%)}
.hero-device{position:absolute;left:122px;top:75px;width:380px;height:220px;border-radius:18px;
  background:linear-gradient(135deg,#9ea3a8 0%,#3a3f46 20%,#0f2a44 50%,#1a3c5c 75%,#55595f 100%);
  transform:rotate(-14deg)}
.hero-copy{position:absolute;left:527px;top:62px;width:262px;color:#fff}
.hero-copy h1{font-family:"Roboto Condensed",sans-serif;font-weight:400;font-size:24px;line-height:28px;
  text-transform:uppercase;white-space:nowrap;letter-spacing:-0.2px}
.hero-copy p{margin-top:6px;font-size:10.2px;line-height:17.5px;color:#ddd}
.btn-more{position:absolute;left:534px;top:282px;width:66px;height:24px;background:var(--red);
  transform:skewX(-20deg);color:#fff;text-align:center;line-height:24px;
  font-family:"Roboto Condensed",sans-serif;font-weight:700;font-size:13px}
.btn-more span{display:inline-block;transform:skewX(20deg)}

/* welcome band */
.welcome-band{position:absolute;left:0;top:438px;width:897px;height:183px;background:var(--light)}
.welcome-band h2{position:absolute;left:105px;top:38px;font-family:"Roboto Condensed",sans-serif;font-weight:400;font-size:23px;color:var(--red-text)}
.welcome-band .intro{position:absolute;left:105px;top:74px;width:452px;font-size:9.5px;line-height:15.2px}
.section-title{font-family:"Roboto Condensed",sans-serif;font-weight:400;font-size:20px;color:var(--ink)}
.news{position:absolute;left:581px;top:38px;width:212px}
.news-thumb{position:absolute;left:1px;top:32px;width:56px;height:70px;border:3px solid #ddd;
  background:linear-gradient(#3a0a0a,#c8301a 50%,#2a0505)}
.news-date{position:absolute;left:82px;top:31px;font-size:10px;color:#aaa;display:flex;align-items:center;gap:4px}
.news-head{position:absolute;left:82px;top:50px;font-family:"Roboto Condensed",sans-serif;font-size:12.5px;color:var(--red-text);white-space:nowrap}
.news-text{position:absolute;left:82px;top:68px;width:132px;font-size:9.6px;line-height:15.2px}
.news-text a{color:var(--red-text);text-decoration:none}

/* testimonials band */
.testi-band{position:absolute;left:0;top:621px;width:897px;height:282px;background:var(--grey-band)}
.testi-band .t-title{position:absolute;left:105px;top:18px}
.quote-box{position:absolute;left:105px;top:49px;width:455px;height:108px;background:#fff;border:1px solid #e2e2e2}
.quote-box p{position:absolute;left:32px;top:14px;width:410px;font-size:9.6px;line-height:15.6px}
.quote-mark{position:absolute;left:8px;top:6px}
.quote-tail{position:absolute;left:148px;top:156px}
.client{position:absolute;top:174px;width:90px;text-align:center;font-size:9.6px}
.avatar{width:62px;height:62px;margin:0 auto 10px;border-radius:50%;background:#d4e6ee;padding:6px}
.avatar div{width:50px;height:50px;border-radius:50%;background:linear-gradient(#b89070,#2a2e36)}
.offer{position:absolute;left:581px;top:18px;width:212px}
.offer-img{position:absolute;left:1px;top:33px;width:210px;height:107px;overflow:hidden;
  background:linear-gradient(90deg,#6a6e64,#1d2a38 30%,#2a4866 60%,#5a5e58)}
.offer-text{position:absolute;left:0;top:145px;width:212px;font-size:9.6px;line-height:15.2px}
.btn-green{position:absolute;left:0;top:203px;width:211px;height:39px;border:2px solid #8ec53e;
  background:linear-gradient(#6bae22,#4a8714);color:#fff;font-family:"Roboto Condensed",sans-serif;
  font-weight:700;font-size:13px;line-height:35px;padding-left:12px}
.btn-green svg{position:absolute;right:16px;top:6px}

/* download band */
.cta-band{position:absolute;left:0;top:903px;width:897px;height:60px;background:linear-gradient(#d0142e,#a80b20)}
.cta-text{position:absolute;left:126px;top:16px;font-family:"Roboto Condensed",sans-serif;font-weight:700;font-size:20px;color:#fff;white-space:nowrap}
.cta-text em{font-style:normal;color:var(--yellow)}
.btn-download{position:absolute;left:603px;top:10px;width:172px;height:37px;border-radius:4px;
  background:linear-gradient(#ffd43a,#f0a500);border:1px solid #fff3b0;
  font-family:"Roboto Condensed",sans-serif;font-size:19px;color:#222;text-align:center;line-height:35px}

/* footer */
.site-footer{position:absolute;left:0;top:963px;width:897px;height:202px;background:var(--footer)}
.zigzag{position:absolute;left:0;top:-1px}
.f-col{position:absolute;top:24px}
.f-col h3{font-family:"Roboto Condensed",sans-serif;font-weight:400;font-size:17px;color:#fff;margin-bottom:6px}
.f-col li{list-style:none;font-size:9.3px;line-height:18.2px;color:var(--footer-link)}
.addr h4{font-family:"Roboto Condensed",sans-serif;font-weight:400;font-size:13px;color:#fff;margin-top:2px}
.addr p{font-size:9.3px;line-height:15.5px;color:var(--footer-link);margin-bottom:8px;white-space:nowrap}
.badge{width:76px;height:44px;border-radius:50%;background:radial-gradient(#d8a640,#7a5410);margin:8px 0 0 12px}
.footer-bar{position:absolute;left:0;top:1165px;width:897px;height:35px;background:var(--footer-bar)}
.footer-bar p{position:absolute;left:105px;top:10px;font-size:9.8px;color:#aaa}
.social{position:absolute;right:104px;top:8px;display:flex;gap:7px}
.social span{width:19px;height:19px;border-radius:50%;background:#3a3a3a}
</style>
</head>
<body>

<header class="site-header">
  <div class="brand"><span class="brand-dot"></span>V7</div>
  <div class="call">Call Us: (555) 0142-7781</div>
  <nav class="main-nav">
    <a class="active nav-home" href="#"><span>Home</span></a>
    <a class="nav-who" href="#"><span>Who We are</span></a>
    <a class="nav-offer" href="#"><span>What We offer</span></a>
    <a class="nav-support" href="#"><span>Support</span></a>
    <a class="nav-contact" href="#"><span>Contact Us</span></a>
  </nav>
</header>

<section class="hero">
  <div class="hero-device" role="img" aria-label="Copier touchscreen control panel"></div>
  <div class="hero-copy">
    <h1>Powerful Performance<br>Enhanced Oerability<br>Energy Efficiency</h1>
    <p>Lorem Ipsum. Proin gravida nibh vel velit auctor aliquet. Aenean sollicitudin, lorem quis bibendum auctor, nisi elit consequat ipsum, nec sagittis sem nibh id elit. Duis sed odio sit amet nibh vulputate cursus a sit amet mauris. Morbi accumsan ipsum velit. Nam nec tellus a odio tincidunt auctor a ornare odio.</p>
  </div>
  <div class="btn-more"><span>More</span></div>
</section>

<section class="welcome-band">
  <h2>Welcome to V7</h2>
  <p class="intro">Lorem Ipsum is simply dummy text of the printing and typesetting industry. Lorem Ipsum has been the industry's standard dummy text ever since the 1500s, when an unknown printer took a galley of type and scrambled it to make a type specimen book. It has survived not only five centuries, but also the leap into electronic typesetting, remaining essentially unchanged. Lorem Ipsum is simply dummy text of the printing and typesetting industry.</p>
  <div class="news">
    <h3 class="section-title">Latest News</h3>
    <div class="news-thumb" role="img" aria-label="Glowing news sign"></div>
    <div class="news-date">
      <svg width="10" height="10" viewBox="0 0 10 10"><rect x="0.5" y="1.5" width="9" height="8" fill="none" stroke="#bbb"/><line x1="0.5" y1="4" x2="9.5" y2="4" stroke="#bbb"/></svg>15 Oct 2013</div>
    <div class="news-head">Lorem ipsum dolor amet</div>
    <p class="news-text">Lorem Ipsum is simply dummy text of the printing and dummy... &nbsp;<a href="#">[Read More]</a></p>
  </div>
</section>

<section class="testi-band">
  <h3 class="section-title t-title">Testimonials</h3>
  <div class="quote-box">
    <svg class="quote-mark" width="18" height="14" viewBox="0 0 18 14"><path d="M0 14V7Q0 1 7 0v3Q3 4 3 7h4v7zM10 14V7q0-6 7-7v3q-4 1-4 4h4v7z" fill="#e3e3e3"/></svg>
    <p>Lorem Ipsum is simply dummy text of the prineting and typesetting industry. Lorem Ipsum has been the induustry's standard dummy text ever since the 1500s, when and unknown printer took a galley of type and scramble it to make a all of type specimen book. It has survived not only five centu all ries, but also the leap into electronic typesetting. Lorem Ipsum is simply dummy text.</p>
  </div>
  <svg class="quote-tail" width="16" height="10" viewBox="0 0 16 10"><path d="M0 1L8 9L16 1" fill="#fff" stroke="#e2e2e2"/><line x1="0" y1="1" x2="16" y2="1" stroke="#fff" stroke-width="2"/></svg>
  <div class="client" style="left:113px"><div class="avatar"><div role="img" aria-label="Client portrait"></div></div>-Clients Name</div>
  <div class="client" style="left:210px"><div class="avatar"><div role="img" aria-label="Client portrait"></div></div>-Clients Name</div>
  <div class="client" style="left:307px"><div class="avatar"><div role="img" aria-label="Client portrait"></div></div>-Clients Name</div>
  <div class="client" style="left:404px"><div class="avatar"><div role="img" aria-label="Client portrait"></div></div>-Clients Name</div>

  <div class="offer">
    <h3 class="section-title">What We offer</h3>
    <div class="offer-img" role="img" aria-label="Copier touchscreen panel close-up">
      <svg width="70" height="70" viewBox="0 0 70 70" style="position:absolute;left:0;top:0"><path d="M0 28L28 0H52L0 52z" fill="var(--red)"/><text x="8" y="42" transform="rotate(-45 20 30)" fill="#fff" font-family="Roboto Condensed, sans-serif" font-size="11">10% Off</text></svg>
    </div>
    <p class="offer-text">Lorem Ipsum is simply dummy text of all the prineting and typesetting industry.</p>
    <div class="btn-green">Toner Recycle Programs
      <svg width="26" height="26" viewBox="0 0 26 26"><path d="M13 3l5 8h-4v2h-2v-2H8z M4 20l4-7 2 3-1 2h6v3H6z M22 20h-6v-3h4l-2-3 3-2 3 5z" fill="#c9f19a"/></svg>
    </div>
  </div>
</section>

<section class="cta-band">
  <div class="cta-text"><em>Download Drivers Software</em> View Norden Model Brochures</div>
  <div class="btn-download">Download Now</div>
</section>

<footer class="site-footer">
  <svg class="zigzag" width="897" height="8" viewBox="0 0 897 8" preserveAspectRatio="none">
    <path d="M0 0H897V0 L893 7 L886 0 L879 7 L872 0 L865 7 L858 0 L851 7 L844 0 L837 7 L830 0 L823 7 L816 0 L809 7 L802 0 L795 7 L788 0 L781 7 L774 0 L767 7 L760 0 L753 7 L746 0 L739 7 L732 0 L725 7 L718 0 L711 7 L704 0 L697 7 L690 0 L683 7 L676 0 L669 7 L662 0 L655 7 L648 0 L641 7 L634 0 L627 7 L620 0 L613 7 L606 0 L599 7 L592 0 L585 7 L578 0 L571 7 L564 0 L557 7 L550 0 L543 7 L536 0 L529 7 L522 0 L515 7 L508 0 L501 7 L494 0 L487 7 L480 0 L473 7 L466 0 L459 7 L452 0 L445 7 L438 0 L431 7 L424 0 L417 7 L410 0 L403 7 L396 0 L389 7 L382 0 L375 7 L368 0 L361 7 L354 0 L347 7 L340 0 L333 7 L326 0 L319 7 L312 0 L305 7 L298 0 L291 7 L284 0 L277 7 L270 0 L263 7 L256 0 L249 7 L242 0 L235 7 L228 0 L221 7 L214 0 L207 7 L200 0 L193 7 L186 0 L179 7 L172 0 L165 7 L158 0 L151 7 L144 0 L137 7 L130 0 L123 7 L116 0 L109 7 L102 0 L95 7 L88 0 L81 7 L74 0 L67 7 L60 0 L53 7 L46 0 L39 7 L32 0 L25 7 L18 0 L11 7 L4 0 L0 4z" fill="#a80b20"/>
  </svg>
  <div class="f-col" style="left:105px"><h3>Who We are</h3><ul><li>Our Philosophy</li><li>Our Values</li><li>Bill of Rights</li><li>Testimonials</li><li>Find Us</li></ul></div>
  <div class="f-col" style="left:305px"><h3>Support</h3><ul><li>Brochures</li><li>Manuals</li><li>Drivers</li><li>Troubleshooting</li><li>Toner Recycle</li></ul></div>
  <div class="f-col" style="left:478px"><h3>What We offer</h3><ul><li>Copiers</li><li>Fax Machines</li></ul>
    <h3 style="margin-top:18px">IT Friendliness</h3><div class="badge" role="img" aria-label="Certification badge"></div></div>
  <div class="f-col addr" style="left:648px">
    <h3><svg width="11" height="15" viewBox="0 0 11 15" style="margin-right:6px;vertical-align:-1px"><path d="M5.5 0A5.5 5.5 0 0 0 0 5.5C0 9 5.5 15 5.5 15S11 9 11 5.5A5.5 5.5 0 0 0 5.5 0zm0 8a2.5 2.5 0 1 1 0-5 2.5 2.5 0 0 1 0 5z" fill="#555"/></svg>Address</h3>
    <h4 style="margin-left:17px">Greenville</h4>
    <p style="margin-left:17px">418-B Marlow Lane<br>Greenville, SC 29601<br>(864) 555-0187</p>
    <h4 style="margin-left:17px">Charlotte</h4>
    <p style="margin-left:17px">2290-D Tallis Road Charlotte,<br>NC 28203<br>(980) 555-0123</p>
  </div>
</footer>

<div class="footer-bar">
  <p>Copyright &copy; &nbsp;2013 V-Seven. All Rights Reserved.</p>
  <div class="social"><span></span><span></span><span></span></div>
</div>

</body>
</html>
```